New business card with our logo

we finalized our logo with the help of pixel harbor - now we need a business card using that logo. we are a metal service center providing raw steel and metal products for fabricating, contractors, artists, etc. we have the wording for the back of the card figured out (attached, no deviations from text please), just need help putting it all together.
would like the look of steel somehow incorporated in the design ... would like the black part of the logo to be steel or silver color (the S & BRANLEY)
Other font styles liked:
- calibri, arial, similar to those, modern looking
Colors
Designer to choose colors to be used in the design.
Requirements
Must have
- Back of card must haves are attached (no deviations from wording please).
- FRONT of card:
- logo
- address
- name
- office tel
- cell
- fax
- website
- address
Nice to have
- incorporate the look of steel or element of steel somehow
- names of the staff on front not in all caps, i.e. Rosvita not ROSVITA
- this industry is more industrial, not coffee or flower shop so design should be aligned with that
- design should be classic and tasteful

```html
<!DOCTYPE html>
<html lang="en">
<head>
<meta charset="utf-8">
<title>Branley Steel – Business Card</title>
<link rel="stylesheet" href="https://fonts.googleapis.com/css2?family=Open+Sans:ital,wght@0,400;0,600;0,700;1,400;1,600&family=Roboto:wght@400;500;700&display=swap">
<style>
  :root {
    --page-bg: #2b2b2d;
    --card-dark: #5a5b5e;
    --card-mid: #6e6f73;
    --steel-light: #c9cacd;
    --steel-shine: #e6e7e9;
    --brand-blue: #1a6fd0;
    --ink: #1e1f21;
    --ink-soft: #2f3033;
    --text-light: #f2f3f5;
    --divider: #2a2b2d;
  }
  * { box-sizing: border-box; margin: 0; padding: 0; }
  html, body {
    width: 1200px; height: 900px; overflow: hidden;
    background: var(--page-bg);
  }
  .canvas { position: relative; width: 1200px; height: 900px; }

  .card {
    position: absolute;
    width: 560px; height: 320px;
    border-radius: 26px;
    overflow: hidden;
    box-shadow: 0 18px 40px rgba(0,0,0,.45);
  }

  /* ---------- Back ---------- */
  .card-back {
    left: 580px; top: 90px;
    background: linear-gradient(135deg, #77787c 0%, var(--card-mid) 45%, #58595c 100%);
    color: var(--text-light);
    font-family: "Open Sans", sans-serif;
    text-align: center;
    padding-top: 42px;
  }
  .brand {
    display: inline-flex; align-items: center; gap: 12px;
    font-family: "Open Sans", sans-serif;
    font-weight: 700;
    letter-spacing: 1px;
    color: var(--ink-soft);
  }
  .brand-dot {
    border-radius: 50%;
    background: var(--brand-blue);
  }
  .card-back .brand { font-size: 40px; }
  .card-back .brand-dot { width: 30px; height: 30px; }
  .service-title {
    margin-top: 14px;
    font-size: 23px; font-weight: 700; letter-spacing: .5px;
    color: var(--text-light);
  }
  .service-tags { font-size: 14px; letter-spacing: .5px; margin-top: 2px; }
  .service-list { margin-top: 18px; font-size: 15px; line-height: 1.45; }
  .service-cta { margin-top: 18px; font-size: 16px; font-weight: 600; }

  /* ---------- Front ---------- */
  .card-front {
    left: 60px; top: 490px;
    background: var(--card-dark);
    font-family: "Roboto", sans-serif;
  }
  .steel-band {
    position: absolute; left: 0; right: 0; top: 34px; height: 222px;
    background: linear-gradient(100deg, #a9aaae 0%, var(--steel-light) 30%, var(--steel-shine) 55%, #b9babd 80%, #a3a4a8 100%);
  }
  .card-front .brand {
    position: absolute; left: 150px; top: 54px;
    font-size: 32px;
  }
  .card-front .brand-dot { width: 26px; height: 26px; }

  .person {
    position: absolute; left: 48px; top: 118px;
    color: var(--ink);
  }
  .person-name { font-size: 26px; font-weight: 700; color: var(--brand-blue); }
  .person-role { font-size: 15px; margin-bottom: 8px; }
  .person-address { font-size: 15px; line-height: 1.35; font-weight: 500; }

  .front-divider {
    position: absolute; left: 262px; top: 122px;
    width: 2px; height: 118px; background: var(--divider);
  }

  .contacts {
    position: absolute; left: 284px; top: 124px;
    list-style: none;
    color: var(--ink);
    font-size: 17px; font-weight: 500;
  }
  .contacts li { display: flex; align-items: center; gap: 10px; height: 28px; }
  .icon {
    width: 20px; height: 20px; flex: none;
  }

  .website {
    position: absolute; left: 48px; bottom: 22px;
    display: flex; align-items: center; gap: 10px;
    color: var(--text-light);
    font-size: 18px; font-weight: 500;
  }
</style>
</head>
<body>
<main class="canvas">

  <section class="card card-back" aria-label="Back of business card">
    <div class="brand"><span class="brand-dot"></span>BRANLEY STEEL</div>
    <p class="service-title">METAL SERVICE CENTER</p>
    <p class="service-tags">CUT, SHEAR, PUNCH, LIGHT FAB</p>
    <p class="service-list">Structural steel, Stainless &amp; Aluminum<br>Building Components, Rebar, Decking... and more!</p>
    <p class="service-cta">Cut to size, pick-up or Delivered!</p>
  </section>

  <section class="card card-front" aria-label="Front of business card">
    <div class="steel-band"></div>
    <div class="brand"><span class="brand-dot"></span>BRANLEY STEEL</div>

    <div class="person">
      <p class="person-name">Rosvita Kade</p>
      <p class="person-role">CEO</p>
      <p class="person-address">Your City address<br>Street location<br>NY city, USA</p>
    </div>

    <div class="front-divider"></div>

    <ul class="contacts">
      <li>
        <svg class="icon" viewBox="0 0 20 20" aria-hidden="true"><circle cx="10" cy="10" r="10" fill="#1a6fd0"/><rect x="7" y="4.5" width="6" height="11" rx="1.2" fill="none" stroke="#fff" stroke-width="1.4"/><circle cx="10" cy="13.3" r=".8" fill="#fff"/></svg>
        123 456 789
      </li>
      <li>
        <svg class="icon" viewBox="0 0 20 20" aria-hidden="true"><circle cx="10" cy="10" r="10" fill="#1a6fd0"/><path d="M7 5.5l2 2.2-1 1.4c.7 1.4 1.6 2.3 3 3l1.4-1 2.2 2-1.2 1.6C9.6 14.5 5.5 10.4 5.3 6.7z" fill="#fff"/></svg>
        123 456 789
      </li>
      <li>
        <svg class="icon" viewBox="0 0 20 20" aria-hidden="true"><circle cx="10" cy="10" r="10" fill="#1a6fd0"/><rect x="6.5" y="4.5" width="7" height="4" fill="#fff"/><rect x="5" y="8.5" width="10" height="5" rx="1" fill="#fff"/><rect x="6.5" y="12" width="7" height="3.5" fill="#fff" stroke="#1a6fd0" stroke-width=".8"/></svg>
        (123)456-789
      </li>
      <li>
        <svg class="icon" viewBox="0 0 20 20" aria-hidden="true"><circle cx="10" cy="10" r="10" fill="#1a6fd0"/><circle cx="10" cy="10" r="2.3" fill="none" stroke="#fff" stroke-width="1.4"/><path d="M12.3 8v3c0 1.6 2.5 1.6 2.5-.8A4.8 4.8 0 1 0 12.5 14" fill="none" stroke="#fff" stroke-width="1.4"/></svg>
        info@branleysteel.com
      </li>
    </ul>

    <div class="website">
      <svg class="icon" viewBox="0 0 20 20" aria-hidden="true"><circle cx="10" cy="10" r="10" fill="#1a6fd0"/><circle cx="10" cy="10" r="5.5" fill="none" stroke="#fff" stroke-width="1.2"/><ellipse cx="10" cy="10" rx="2.3" ry="5.5" fill="none" stroke="#fff" stroke-width="1.1"/><path d="M4.5 10h11M5.5 7.3h9M5.5 12.7h9" stroke="#fff" stroke-width="1"/></svg>
      www.branleysteel.com
    </div>
  </section>

</main>
</body>
</html>
```